Road Construction Company needs business cards

We would like a new business card designed for our business.

We're a road construction company based in Qld, Australia.

Can the business card please have the following information on it.

Name: Brent Malvoy
Position: General Manager
Phone: 0471 592 304
Email: Brent.malvoy@quendix.com.au
Address: 87 Harrowgate Ave, Pindarra, QLD, 4000
Website: www.quendix.com.au

Visually we'd like the card to be professional and simple.

Attached is our logo.

Our website is www.quendix.com.au

Target Market(s)

Men aged 25-60

Contact Information for Business Card

As listed in project description

Font styles to use
Serif

Requirements
Must have
• Large logo on back of card

```html
<!DOCTYPE html>
<html lang="en">
<head>
<meta charset="utf-8">
<title>Quendix Business Card</title>
<link href="https://fonts.googleapis.com/css2?family=Lato:wght@300;400;900&display=swap" rel="stylesheet">
<style>
  :root {
    --page-bg: #d9dde1;
    --card-black: #231f20;
    --brand-blue: #2fa3dc;
    --divider-blue: #1f5f9e;
    --text-white: #ffffff;
  }
  * { box-sizing: border-box; margin: 0; padding: 0; }
  html, body {
    width: 1200px; height: 900px; overflow: hidden;
    background: var(--page-bg);
    font-family: "Lato", sans-serif;
  }
  .sheet {
    width: 1200px; height: 900px;
    display: flex; flex-direction: column;
    align-items: center; justify-content: center; gap: 60px;
  }
  .card {
    position: relative;
    width: 620px; height: 354px;
    background: var(--card-black);
    color: var(--text-white);
    overflow: hidden;
    box-shadow: 0 6px 18px rgba(0,0,0,0.25);
  }
  .wordmark {
    font-family: "Lato", sans-serif;
    font-weight: 900;
    color: var(--text-white);
    text-transform: uppercase;
    letter-spacing: 1px;
    line-height: 1;
  }
  .card-front .wordmark {
    position: absolute; top: 46px; left: 150px;
    font-size: 74px;
  }
  .identity {
    position: absolute; top: 166px; left: 40px; width: 240px;
  }
  .identity .name {
    font-size: 25px; font-weight: 400; text-transform: uppercase;
    letter-spacing: -0.5px;
  }
  .identity .role {
    margin-top: 4px;
    font-size: 19px; font-weight: 300; color: var(--brand-blue);
  }
  .divider {
    position: absolute; top: 164px; left: 284px;
    width: 2px; height: 74px; background: var(--divider-blue);
  }
  .contacts {
    position: absolute; top: 166px; left: 302px;
    list-style: none;
  }
  .contacts li {
    display: flex; align-items: center; gap: 8px;
    height: 24px; font-size: 15px; font-weight: 400;
  }
  .contacts svg { width: 18px; height: 18px; flex: none; }
  .address-band {
    position: absolute; left: 0; right: 0; top: 258px; height: 44px;
    background: var(--brand-blue);
    display: flex; align-items: center; gap: 10px; padding-left: 40px;
    font-size: 16px; font-weight: 400;
  }
  .address-band svg { width: 20px; height: 20px; flex: none; }
  .card-back {
    display: flex; align-items: center; justify-content: center;
  }
  .card-back .wordmark { font-size: 104px; }
</style>
</head>
<body>
<main class="sheet">
  <section class="card card-front" aria-label="Business card front">
    <div class="wordmark">Quendix</div>

    <div class="identity">
      <p class="name">Brent Malvoy</p>
      <p class="role">General Manager</p>
    </div>

    <div class="divider"></div>

    <ul class="contacts">
      <li>
        <svg viewBox="0 0 20 20" aria-hidden="true">
          <circle cx="10" cy="10" r="10" fill="var(--brand-blue)"/>
          <path d="M7 5.5c.6-.3 1.1 0 1.3.5l.6 1.5c.2.5 0 .9-.4 1.2l-.5.4c.5 1.1 1.3 1.9 2.4 2.4l.4-.5c.3-.4.7-.6 1.2-.4l1.5.6c.5.2.8.7.5 1.3-.4 1-1.4 1.6-2.5 1.3C8.8 13.5 6.5 11.2 5.8 8 5.5 6.9 6.1 5.9 7 5.5z" fill="var(--card-black)"/>
        </svg>
        0471 592 304
      </li>
      <li>
        <svg viewBox="0 0 20 20" aria-hidden="true">
          <circle cx="10" cy="10" r="10" fill="var(--brand-blue)"/>
          <text x="10" y="14" text-anchor="middle" font-family="Lato, sans-serif" font-size="12" font-weight="900" fill="var(--card-black)">@</text>
        </svg>
        Brent.malvoy@quendix.com.au
      </li>
      <li>
        <svg viewBox="0 0 20 20" aria-hidden="true">
          <circle cx="10" cy="10" r="10" fill="var(--brand-blue)"/>
          <g fill="none" stroke="var(--card-black)" stroke-width="1.2">
            <circle cx="10" cy="10" r="5.5"/>
            <ellipse cx="10" cy="10" rx="2.4" ry="5.5"/>
            <line x1="4.5" y1="10" x2="15.5" y2="10"/>
          </g>
        </svg>
        www.quendix.com.au
      </li>
    </ul>

    <div class="address-band">
      <svg viewBox="0 0 20 20" aria-hidden="true">
        <circle cx="10" cy="10" r="10" fill="var(--text-white)"/>
        <path d="M10 4.5a3.8 3.8 0 0 0-3.8 3.8c0 2.8 3.8 7 3.8 7s3.8-4.2 3.8-7A3.8 3.8 0 0 0 10 4.5zm0 5.3a1.5 1.5 0 1 1 0-3 1.5 1.5 0 0 1 0 3z" fill="var(--brand-blue)"/>
      </svg>
      87 Harrowgate Ave, Pindarra, QLD, 4000
    </div>
  </section>

  <section class="card card-back" aria-label="Business card back">
    <div class="wordmark">Quendix</div>
  </section>
</main>
</body>
</html>
```